Copper Heron Motor Services needs a logo design

I'm after a logo design for a new Female owned automotive repair workshop in the Queanbeyan/Canberra Australia Area.
We offer repairs on all passenger cars, 4wds and light trucks emphasising a strong honest work ethic and a genuine interest in the customer and their vehicles needs. With business details on the front of the card and what we offer on the back.
I would like a design with a phoenix in multiple colours maybe hovering over a flaming wheel or a car with wheels flaming with the phoenix hovering up out of the flames
Target Market(s)
All Vehicle users
Industry/Entity Type
Automotive
Contact Information for Business Card
On the front
Copper Heron Motor
Maree Tolland Owner/ Mechanic 0413527806
email maree@copperheronmotor.com.au
Website www.copperheronmotorworks.com.au
On the back
All Cars, 4WDs, Light trucks, makes and models
Log book servicing
General vehicle servicing
Major vehicle servicing
brake and clutch servicing and repairs
Suspension repairs
cooling systems
All major and minor mechanical repairs
minor electrical rewiring and repairs
Colors
Designer to choose colors to be used in the design.
Look and feel

```html
<!DOCTYPE html>
<html lang="en">
<head>
<meta charset="utf-8">
<title>Copper Heron Motor – Business Card</title>
<link href="https://fonts.googleapis.com/css2?family=Michroma&family=Roboto+Condensed:wght@300;400&display=swap" rel="stylesheet">
<style>
  :root {
    --page: #e4e4e4;
    --card: #050505;
    --band-dark: #2a0204;
    --band-mid: #5e0a0e;
    --band-line: #8a1218;
    --silver: #d6d6d8;
    --text-light: #f2f2f2;
    --text-soft: #c9c9c9;
    --mark-square: #b0171f;
  }
  * { margin: 0; padding: 0; box-sizing: border-box; }
  html, body { width: 1200px; height: 1200px; overflow: hidden; }
  body {
    background: var(--page);
    display: flex;
    flex-direction: column;
    align-items: center;
    justify-content: center;
    gap: 56px;
  }
  .card {
    position: relative;
    width: 860px;
    height: 526px;
    background: var(--card);
    overflow: hidden;
    box-shadow: 0 14px 30px rgba(0,0,0,0.22);
  }
  .band {
    position: absolute;
    left: 0;
    width: 100%;
    height: 118px;
    background: linear-gradient(90deg, var(--card) 0%, var(--band-dark) 22%, var(--band-mid) 55%, var(--band-dark) 85%, var(--card) 100%);
    border-top: 2px solid var(--band-line);
    border-bottom: 2px solid var(--band-line);
    display: flex;
    align-items: center;
    padding-left: 60px;
  }
  .wordmark {
    display: flex;
    align-items: center;
    gap: 16px;
    font-family: "Roboto Condensed", sans-serif;
    font-weight: 400;
    font-size: 42px;
    color: var(--text-light);
    white-space: nowrap;
  }
  .wordmark-square {
    width: 22px;
    height: 22px;
    background: var(--mark-square);
  }

  /* front */
  .card-front .band { top: 72px; }
  .person {
    position: absolute;
    top: 232px;
    right: 60px;
    text-align: right;
  }
  .person-name {
    font-family: "Michroma", sans-serif;
    font-size: 34px;
    color: var(--silver);
    letter-spacing: 1px;
  }
  .person-role {
    font-family: "Roboto Condensed", sans-serif;
    font-weight: 300;
    font-size: 24px;
    color: var(--text-soft);
    margin-top: 12px;
  }
  .contact {
    position: absolute;
    bottom: 44px;
    display: flex;
    align-items: center;
    gap: 12px;
    font-family: "Roboto Condensed", sans-serif;
    font-weight: 300;
    font-size: 26px;
    color: var(--text-light);
  }
  .contact-phone { left: 48px; }
  .contact-email { right: 48px; }
  .contact svg { width: 24px; height: 24px; fill: var(--text-light); }

  /* back */
  .card-back .band { top: 318px; }
  .services {
    position: absolute;
    top: 56px;
    left: 0;
    width: 100%;
    list-style: none;
    text-align: center;
    font-family: "Roboto Condensed", sans-serif;
    font-weight: 300;
    font-size: 24px;
    line-height: 40px;
    color: var(--text-light);
  }
</style>
</head>
<body>

  <section class="card card-front" aria-label="Business card front">
    <div class="band">
      <div class="wordmark"><span class="wordmark-square"></span><span>Copper Heron Motor</span></div>
    </div>
    <div class="person">
      <div class="person-name">MAREE TOLLAND</div>
      <div class="person-role">Owner/ Mechanic</div>
    </div>
    <div class="contact contact-phone">
      <svg viewBox="0 0 24 24" aria-hidden="true"><path d="M6.6 10.8c1.4 2.8 3.8 5.1 6.6 6.6l2.2-2.2c.3-.3.7-.4 1-.2 1.1.4 2.3.6 3.6.6.6 0 1 .4 1 1V20c0 .6-.4 1-1 1C10.6 21 3 13.4 3 4c0-.6.4-1 1-1h3.5c.6 0 1 .4 1 1 0 1.3.2 2.5.6 3.6.1.3 0 .7-.2 1l-2.3 2.2z"/></svg>
      <span>0413527806</span>
    </div>
    <div class="contact contact-email">
      <svg viewBox="0 0 24 24" aria-hidden="true"><path d="M3 5h18v14H3V5zm2 2v.4l7 4.6 7-4.6V7H5zm14 2.8-7 4.6-7-4.6V17h14V9.8z"/></svg>
      <span>maree@copperheronmotor.com.au</span>
    </div>
  </section>

  <section class="card card-back" aria-label="Business card back">
    <ul class="services">
      <li>All Cars, 4wds, Light Trucks, Makes And Models | Log Book Servicing</li>
      <li>General Vehicle Servicing | Major Vehicle Servicing</li>
      <li>Brake And Clutch Servicing And Repairs | Suspension Repairs | Cooling Systems</li>
      <li>All Major And Minor Mechanical Repairs</li>
      <li>Minor Electrical Rewiring And Repairs</li>
    </ul>
    <div class="band">
      <div class="wordmark"><span class="wordmark-square"></span><span>Copper Heron Motor</span></div>
    </div>
  </section>

</body>
</html>
```